Business Consulting Business Card

professional business card with basic information (1) First and Last name (2) email address, (3) phone number, (4) website.

```html
<!DOCTYPE html>
<html lang="en">
<head>
<meta charset="utf-8">
<title>Tidewell Business Card</title>
<link href="https://fonts.googleapis.com/css2?family=Montserrat:wght@400;500;700&display=swap" rel="stylesheet">
<style>
  :root {
    --navy: #0d2b42;
    --navy-soft: #17394f;
    --teal: #4fb3c8;
    --teal-light: #5ec9c4;
    --white: #ffffff;
    --ink: #0d2b42;
    --grey-text: #3b4650;
    --rule: #cfe7ee;
    --backdrop: #e9ecef;
  }
  * { margin: 0; padding: 0; box-sizing: border-box; }
  html, body {
    width: 1200px; height: 909px; overflow: hidden;
    background: var(--backdrop);
    font-family: "Montserrat", sans-serif;
  }
  .canvas { position: relative; width: 1200px; height: 909px; }

  .card {
    position: absolute;
    width: 540px; height: 310px;
    border-radius: 22px;
    overflow: hidden;
    box-shadow: 0 10px 28px rgba(13, 43, 66, 0.22);
  }

  /* Back side */
  .card-back {
    left: 70px; top: 120px;
    background: linear-gradient(135deg, var(--navy-soft), var(--navy));
    display: flex; align-items: center; justify-content: center; gap: 22px;
  }
  .brand-dot {
    width: 58px; height: 58px; border-radius: 50%;
    background: var(--teal);
  }
  .brand-name {
    color: var(--white);
    font-weight: 400; font-size: 40px; letter-spacing: 12px;
  }

  /* Front side */
  .card-front {
    left: 590px; top: 470px;
    background: var(--white);
  }
  .front-wave { position: absolute; left: 0; bottom: 0; width: 540px; height: 150px; }
  .front-brand {
    position: absolute; right: 34px; top: 30px;
    display: flex; align-items: center; gap: 10px;
  }
  .front-brand .brand-dot { width: 30px; height: 30px; }
  .front-brand .brand-name { color: var(--ink); font-size: 20px; letter-spacing: 5px; }
  .top-rule {
    position: absolute; left: 150px; right: 34px; top: 92px;
    height: 1px; background: var(--rule);
  }
  .address {
    position: absolute; right: 34px; top: 108px;
    text-align: right; color: var(--grey-text);
    font-size: 12px; line-height: 1.45;
  }
  .identity { position: absolute; left: 34px; top: 128px; }
  .person-name { color: var(--ink); font-weight: 700; font-size: 22px; letter-spacing: 1px; }
  .person-role { color: var(--grey-text); font-size: 13px; margin-top: 2px; }
  .id-rule { width: 200px; height: 1px; background: var(--rule); margin: 12px 0 10px; }
  .contacts { list-style: none; font-size: 12.5px; color: var(--grey-text); }
  .contacts li { display: flex; align-items: center; gap: 8px; line-height: 1.6; }
  .contacts svg { width: 11px; height: 11px; fill: var(--ink); }
</style>
</head>
<body>
<main class="canvas">
  <section class="card card-back">
    <span class="brand-dot"></span>
    <span class="brand-name">TIDEWELL</span>
  </section>

  <section class="card card-front">
    <div class="front-brand">
      <span class="brand-dot"></span>
      <span class="brand-name">TIDEWELL</span>
    </div>
    <div class="top-rule"></div>
    <p class="address">1480 W Harbor street<br>Bellmont County name 7714</p>

    <div class="identity">
      <h1 class="person-name">MARTEN OLSEN</h1>
      <p class="person-role">General Manager</p>
      <div class="id-rule"></div>
      <ul class="contacts">
        <li><svg viewBox="0 0 24 24"><path d="M6.6 10.8a15 15 0 0 0 6.6 6.6l2.2-2.2a1 1 0 0 1 1-.25 11.4 11.4 0 0 0 3.6.57 1 1 0 0 1 1 1V20a1 1 0 0 1-1 1A17 17 0 0 1 3 4a1 1 0 0 1 1-1h3.5a1 1 0 0 1 1 1c0 1.25.2 2.45.57 3.57a1 1 0 0 1-.25 1z"/></svg>555-210-4837</li>
        <li><svg viewBox="0 0 24 24"><path d="M2 5h20v14H2z M2 5l10 8 10-8" /></svg>info@tidewell.com</li>
        <li><svg viewBox="0 0 24 24"><circle cx="12" cy="12" r="10"/></svg>www.tidewell.com</li>
      </ul>
    </div>

    <svg class="front-wave" viewBox="0 0 540 150" preserveAspectRatio="none" aria-hidden="true">
      <path d="M0 140 C150 120 230 100 320 40 C390 0 470 -5 540 2 L540 150 L0 150 Z" fill="var(--teal)"/>
      <path d="M0 146 C160 128 240 110 330 52 C400 12 470 6 540 10 L540 150 L0 150 Z" fill="var(--white)"/>
      <path d="M0 150 C170 136 250 118 340 62 C410 22 475 14 540 16 L540 150 Z" fill="var(--navy)"/>
    </svg>
  </section>
</main>
</body>
</html>
```